Referral Card thats different from the rest

Business card size-

Referral card that will be given to clients, in turn they will pass it on to their friends.

The referee will add their name and address, and friends name to card before it is passed on

Referee gets 2 FREE movie tickets

Friend gets $25 OFF their service

Company is an electrical contracting company specialising in the domestic market.

I would like the card to be fun not so serious!
Completely open minded to any and every creative idea!

attached is 2 photo of an example of what another business has, i am trying to achieve something similiar
Updates

I have increased the budget, ;)

i have added 2 x photos of what i am trying to achieve. this is from another business, I am after something similar to this
Thanks

I have updated the design brief.
this should help make it easir and more clear
Thanks

Target Market(s)

Home owners from 30yrs +

Industry/Entity Type

Electrical

Requirements
Must have
• Logo - Not a main feature of card
1300 846 572 on both sides
Lic no: 418695D (doesn’t have to be big) prefer on back

The main feature of the front of the card is the 2 free movie tickets for Referee & $25 OFF Friends first bill

HOW ABOUT TWO FREE MOVIE TICKETS?
It is easy! Know someone who needs an electrician? Maybe a friend, family member, relative or work colleague.
Tell them about us, and we will take $25 off their first bill and give you two FREE Movie Tickets just for introducing us.
To make a referral fill out this card and give it to your friend.

Recommended By:____________
Address:__________________
Frinds name: _____________

*this offer is only valued for work over $55. Non transferable for cash. This coupon is limited to 1 per customer, not to be used in conjunction with any other offer
Nice to have
• Catchy heading on card
example- tell a friend for cash card, (if i was giving away cash vouchers..)

example- keep me in your wallet and pass me on

```html
<!DOCTYPE html>
<html lang="en">
<head>
<meta charset="utf-8">
<title>Tell A Friend Referral Card</title>
<link href="https://fonts.googleapis.com/css2?family=Comfortaa:wght@700&family=Russo+One&family=Alegreya+Sans:wght@400;700&family=Oswald:wght@700&family=Arimo:wght@400&display=swap" rel="stylesheet">
<style>
:root{
  --page:#ffffff;
  --ink:#1a1a1a;
  --red:#e3150d;
  --green-deep:#3f9a0c;
  --green-mid:#7fd31a;
  --green-pale:#dff5b8;
  --parrot-yellow:#d8e82a;
  --parrot-green:#5fbf2a;
  --perch:#7a3a1c;
  --fish-red:#ec2a18;
  --fish-pink:#f07a8c;
  --fish-blue:#2a3fd6;
  --fish-navy:#1a237e;
  --rule:#222222;
}
*{box-sizing:border-box;margin:0;padding:0}
html,body{width:1200px;height:1079px;overflow:hidden;background:var(--page)}
.canvas{position:relative;width:1200px;height:1079px;background:var(--page)}
.card{position:absolute;background:#fff;overflow:hidden;box-shadow:3px 4px 6px rgba(0,0,0,.35)}
.card--front{left:49px;top:46px;width:865px;height:480px}
.card--back{left:289px;top:563px;width:866px;height:477px}

.swirl{position:absolute;left:0;top:160px;width:865px;height:320px;
  background:radial-gradient(ellipse 70% 40% at 45% 45%,var(--green-mid),transparent 70%),
  linear-gradient(170deg,#fff 5%,var(--green-pale) 30%,var(--green-deep) 55%,var(--green-mid) 70%,#fff 95%);
  opacity:.9}
.front-title{position:absolute;left:24px;top:8px;font-family:"Comfortaa",sans-serif;font-weight:700;font-size:48px;line-height:56px;color:var(--red);white-space:nowrap}
.front-sub{position:absolute;left:34px;top:68px;font-family:"Russo One",sans-serif;font-style:italic;font-size:26px;line-height:30px;color:var(--ink);letter-spacing:1.5px;white-space:nowrap}
.front-sub .accent{color:var(--red)}
.body-copy{position:absolute;font-family:"Alegreya Sans",sans-serif;font-size:27px;line-height:32px;color:var(--ink);white-space:nowrap}
.body-copy span{display:block}
.body-copy--intro{left:0;top:100px;width:614px;text-align:right}
.body-copy--offer{left:6px;top:178px}
.body-copy--offer .l2{padding-left:16px}
.body-copy--offer .l3{padding-left:22px}
.body-copy--offer .l4{padding-left:182px}
.perch{position:absolute;left:328px;top:336px;width:360px;height:6px;background:var(--perch);border-radius:3px}
.parrot{position:absolute;left:653px;top:52px;width:206px;height:416px;border-radius:48% 40% 30% 30%;
  background:radial-gradient(circle at 40% 30%,var(--parrot-yellow),var(--parrot-green) 70%,#fff 100%)}
.phone{position:absolute;font-family:"Oswald",sans-serif;font-weight:700;font-size:36px;line-height:42px;color:var(--ink);white-space:nowrap;letter-spacing:.5px}
.phone--front{left:435px;top:364px}
.brand{position:absolute;left:14px;top:422px;display:flex;align-items:center;gap:8px}
.brand-dot{width:24px;height:24px;border-radius:50%;background:var(--red)}
.brand-name{font-family:"Alegreya Sans",sans-serif;font-weight:700;font-size:20px;color:var(--ink)}

.back-title{position:absolute;left:38px;top:8px;font-family:"Comfortaa",sans-serif;font-weight:700;font-size:37px;color:var(--red);white-space:nowrap}
.back-intro{position:absolute;left:126px;top:84px;font-family:"Alegreya Sans",sans-serif;font-size:28px;line-height:30px;color:var(--ink)}
.fish{position:absolute}
.fish--red{left:572px;top:60px;width:280px;height:135px;border-radius:50% 30% 30% 50%;
  background:radial-gradient(ellipse at 35% 50%,var(--fish-pink),var(--fish-red) 60%,#fff 100%)}
.fish--blue{left:0;top:300px;width:118px;height:170px;border-radius:30% 50% 40% 10%;
  background:radial-gradient(ellipse at 50% 50%,var(--fish-blue),var(--fish-navy) 80%)}
.field{position:absolute;left:126px;display:flex;align-items:flex-end;font-family:"Alegreya Sans",sans-serif;font-size:28px;color:var(--ink);white-space:nowrap}
.field .line{border-bottom:1.5px solid var(--rule);margin-left:8px;height:24px}
.field--ref{top:180px}.field--ref .line{width:445px}
.field--addr{top:227px}.field--addr .line{width:556px}
.field--friend{top:276px}.field--friend .line{width:501px}
.phone--back{left:584px;top:338px}
.terms{position:absolute;left:159px;top:396px;width:662px;font-family:"Arimo",sans-serif;font-size:17.5px;line-height:21px;color:var(--ink);padding-left:22px}
.terms::before{content:"\2731";position:absolute;left:0;top:2px;font-size:15px}
.licence{position:absolute;right:55px;top:442px;font-family:"Arimo",sans-serif;font-size:17px;color:var(--ink)}
</style>
</head>
<body>
<main class="canvas">
  <section class="card card--front">
    <div class="swirl" role="img" aria-label="Flowing green light swirl background"></div>
    <h1 class="front-title">Tell A Friend for Cash Card</h1>
    <h2 class="front-sub">HOW ABOUT <span class="accent">TWO FREE</span> MOVIE TICKETS?</h2>
    <p class="body-copy body-copy--intro"><span>It is easy! Know someone who needs an electrician?</span><span>Maybe a friend, family member, relative or work</span><span>colleague.</span></p>
    <p class="body-copy body-copy--offer"><span class="l1">Tell them about us, and we will take $25 off their</span><span class="l2">first bill and give you two FREE Movie Tickets</span><span class="l3">just for introducing us. To make a referral fill out</span><span class="l4">this card and give it to your friend.</span></p>
    <div class="perch"></div>
    <div class="parrot" role="img" aria-label="Cartoon green and yellow parrot on a perch pointing at the text"></div>
    <div class="phone phone--front">1300 846 572</div>
    <div class="brand"><span class="brand-dot"></span><span class="brand-name">Bright Spark Electrical</span></div>
  </section>

  <section class="card card--back">
    <h2 class="back-title">Keep me in your wallet and pass me on..</h2>
    <p class="back-intro">To make a referral fill out this card<br>and give it to your friend.</p>
    <div class="fish fish--red" role="img" aria-label="Cartoon red fish"></div>
    <div class="field field--ref">Recommended By:<span class="line"></span></div>
    <div class="field field--addr">Address:<span class="line"></span></div>
    <div class="field field--friend">Friends name:<span class="line"></span></div>
    <div class="fish fish--blue" role="img" aria-label="Cartoon blue fish"></div>
    <div class="phone phone--back">1300 846 572</div>
    <p class="terms">this offer is only valued for work over $55. Non transferable for cash. This coupon is limited to 1 per customer, not to be used in conjunction with any other offer</p>
    <p class="licence">Lic no: 418695D</p>
  </section>
</main>
</body>
</html>
```